We are a Leadership Specialist Boutique Business that is launching a residential womans workshop....

We need a post card which will include our logo, an overview of our workshop, a catch statement on one side and on the other side dates, venue, facilitators and contacts to book the workshop. The postcards will be distributed at an Global Sisterhood Harvest Lunch. They will be placed at each setting of the lunch attendees. The company QBR running the lunch is a sponsor of our business.

Target Market(s)

Women supervisor to middle management positions or own business

Industry/Entity Type

Academic Training

Font styles to use
Serif

Colors
34a7d8

Requirements
Must have
• Use Colour Palette on docs attached, Logo, Workshop overview either the Circle Theory or the Core Philosophy Text,
• The dates, venue, all costs of the program including discount code. One catch sentence that grabs the audience from the content I have provided that appeals to the designer
• Must have these contacts.
• Website: brightpathforwardgroup.com,au
• Email: Info@brightpathforwardgroup.com.au.
• Phone: 0419372605
Nice to have
• Facilitators Photos and names

```html
<!DOCTYPE html>
<html lang="en">
<head>
<meta charset="utf-8">
<title>Core Philosophy Postcard</title>
<link href="https://fonts.googleapis.com/css2?family=Oswald:wght@500;600&family=Lato:ital,wght@0,400;0,700;1,400;1,700&family=Roboto:wght@500;700&display=swap" rel="stylesheet">
<style>
  :root{
    --blue:#34a7d8;
    --blue-deep:#1d6f98;
    --mint:#aeeedb;
    --ink:#2b2b2b;
    --charcoal:#3a3a3a;
    --white:#ffffff;
    --bg:#e4e4e4;
    --gold:#c99a2e;
  }
  *{box-sizing:border-box;margin:0;padding:0}
  html,body{width:1200px;height:1200px;overflow:hidden;background:var(--bg)}
  body{position:relative;font-family:"Lato",sans-serif;color:var(--ink)}
  .card{position:absolute;left:329px;width:542px;height:386px;background:var(--white);overflow:hidden}
  .card--front{top:169px}
  .card--back{top:645px}
  .abs{position:absolute}
  .heading{font-family:"Oswald",sans-serif;font-weight:500;color:var(--blue);text-transform:uppercase;letter-spacing:-.2px}

  /* logo */
  .brand{display:flex;flex-direction:column;align-items:center;justify-content:center}
  .brand__ring{width:84px;height:84px;border:3px solid var(--ink);border-radius:50%;display:flex;align-items:center;justify-content:center}
  .brand__name{font-family:"Lato",sans-serif;font-weight:700;font-size:13px;color:var(--ink);white-space:nowrap}

  /* front */
  .front__logo{left:0;top:0;width:141px;height:138px;background:var(--mint)}
  .front__hero{left:141px;top:0;width:401px;height:138px;background:linear-gradient(120deg,#8fd8c8 0%,#a9e6d6 45%,#7cc3b6 100%)}
  .front__title{left:185px;top:0;width:320px;height:138px;font-family:"Oswald",sans-serif;font-weight:600;text-transform:uppercase}
  .front__title .line{position:absolute;left:0;white-space:nowrap;line-height:1;transform-origin:left top;transform:scale(1,1.25)}
  .front__title .l1{top:20px;font-size:30px;color:var(--blue-deep);letter-spacing:-.4px}
  .front__title .l2{top:62px;font-size:40px;color:var(--ink);letter-spacing:-.6px}
  .why{left:0;top:146px;width:190px;height:89px;background:var(--blue);color:var(--white);padding:10px 14px 0 20px}
  .why .heading{color:var(--white);font-size:12px;margin-bottom:4px}
  .why p{font-size:8.3px;line-height:1.3;text-align:justify}
  .front__photo{left:0;top:235px;width:190px;height:151px;background:linear-gradient(135deg,#d9cfc7,#b89a86 55%,#6f5a63)}
  .points{left:207px;top:152px;width:320px}
  .points .heading{font-size:12px;margin-top:6px}
  .point{display:flex;gap:4px;font-size:10.3px;line-height:1.3;margin-top:3px}
  .tick{flex:none;width:8px;height:8px;margin-top:3px}
  .catch{margin-top:6px;font-style:italic;font-size:12px;line-height:1.3}
  .front__cta{left:190px;top:324px;width:352px;height:48px;background:var(--charcoal);color:var(--white);display:flex;align-items:center;padding-left:17px;gap:16px}
  .front__cta .label{font-size:17px}
  .front__cta .num{font-size:25px;font-weight:700;letter-spacing:.3px}
  .front__strip{left:190px;top:372px;width:352px;height:14px;background:var(--blue)}

  /* back */
  .back__top{left:0;top:0;width:542px;height:18px;background:var(--mint)}
  .back__band{left:0;top:18px;width:542px;height:53px;background:var(--blue)}
  .back__title{left:0;top:18px;width:403px;height:53px;display:flex;align-items:center;justify-content:center;font-family:"Oswald",sans-serif;font-weight:500;font-size:22px;color:var(--white);text-transform:uppercase;letter-spacing:-.3px;padding-left:22px;white-space:nowrap}
  .back__logo{left:403px;top:0;width:123px;height:96px;background:var(--mint)}
  .back__logo .brand__ring{width:62px;height:62px;border-width:2.5px}
  .back__logo .brand__name{font-size:9.5px}
  .left-col{left:14px;top:86px;width:216px}
  .left-col .heading{font-size:11.5px}
  .dates{margin-top:5px;border:1px solid var(--blue);padding:3px 0 4px 18px;font-family:"Roboto",sans-serif;font-weight:500;font-size:17.5px;line-height:1.15}
  .label-it{font-weight:700;font-style:italic;color:var(--blue);font-size:13px;margin-top:8px}
  .info{font-family:"Roboto",sans-serif;font-weight:500;font-size:13px;line-height:1.25}
  .left-col .heading.sub{margin-top:6px}
  .small{font-size:8.3px;line-height:1.3;text-align:justify;margin-top:2px}
  .right-col{left:251px;top:91px;width:280px}
  .right-col .heading{font-size:11.5px}
  .price{margin-top:7px;display:flex;align-items:baseline;gap:5px;font-family:"Roboto",sans-serif;font-weight:700;white-space:nowrap}
  .price .full{font-size:18px}
  .price .note{font-size:9px}
  .price .early{font-size:18px;color:var(--blue)}
  .quote{margin-top:6px;font-family:"Roboto",sans-serif;font-weight:500;font-size:10.5px;line-height:1.3}
  .seal{left:416px;top:136px;width:52px;height:52px}
  .facilitator{top:192px;width:140px;text-align:center}
  .facilitator__photo{width:76px;height:76px;border-radius:50%;margin:0 auto;background:radial-gradient(circle at 50% 40%,#d8d8d8,#8a8a8a)}
  .facilitator__name{font-size:13.5px;margin-top:2px}
  .facilitator__role{font-size:8.5px;line-height:1.3}
  .back__cta{left:0;top:320px;width:252px;height:52px;background:var(--blue);color:var(--white);padding:6px 0 0 47px}
  .back__cta .label{font-size:17px;line-height:1}
  .back__cta .num{display:flex;align-items:center;gap:5px;font-size:21px;font-weight:700;margin-top:3px}
  .back__cta .num svg{width:15px;height:15px}
  .back__contact{left:252px;top:320px;width:290px;height:52px;background:var(--mint);padding:6px 0 0 58px;font-size:10.3px}
  .contact-row{display:flex;align-items:center;gap:8px;height:20px}
  .contact-row svg{width:14px;height:14px;flex:none}
  .back__strip-a{left:0;top:372px;width:252px;height:14px;background:var(--mint)}
  .back__strip-b{left:252px;top:372px;width:290px;height:14px;background:var(--blue)}
</style>
</head>
<body>

<section class="card card--front">
  <div class="abs front__logo brand"><div class="brand__ring"><span class="brand__name">brightpath</span></div></div>
  <div class="abs front__hero" role="img" aria-label="Teal-tinted photo of women working together in a bright studio"></div>
  <h1 class="abs front__title"><span class="line l1">The Core Philosophy</span><span class="line l2">of the Program</span></h1>

  <div class="abs why">
    <h2 class="heading">Why choose us</h2>
    <p>The program is emersive and wholistic which includes development of yOur life and leadership skills, by rewriting your narrative and a personal action plan for change</p>
  </div>
  <div class="abs front__photo" role="img" aria-label="Photo of a smiling businesswoman standing in her clothing boutique"></div>

  <div class="abs points">
    <h2 class="heading">Worldview</h2>
    <p class="point"><svg class="tick" viewBox="0 0 10 10"><circle cx="5" cy="5" r="5" fill="#34a7d8"/><path d="M2.8 5.2l1.5 1.5 3-3" stroke="#fff" stroke-width="1.3" fill="none"/></svg>A view Held inside of us as to how things work</p>
    <h2 class="heading">Biases</h2>
    <p class="point"><svg class="tick" viewBox="0 0 10 10"><circle cx="5" cy="5" r="5" fill="#34a7d8"/><path d="M2.8 5.2l1.5 1.5 3-3" stroke="#fff" stroke-width="1.3" fill="none"/></svg>Our own behaviours and the behaviours of others that reinforce this&nbsp; worldviews</p>
    <h2 class="heading">Error Scripts</h2>
    <p class="point"><svg class="tick" viewBox="0 0 10 10"><circle cx="5" cy="5" r="5" fill="#34a7d8"/><path d="M2.8 5.2l1.5 1.5 3-3" stroke="#fff" stroke-width="1.3" fill="none"/></svg>Stories implanted by us or others that limits our potential</p>
    <p class="catch">Rewiting a new Personal Narrative allows us to shatter our own glass celing</p>
  </div>

  <div class="abs front__cta"><span class="label">CONTACTS US NOW</span><span class="num">0419372605</span></div>
  <div class="abs front__strip"></div>
</section>

<section class="card card--back">
  <div class="abs back__top"></div>
  <div class="abs back__band"></div>
  <h1 class="abs back__title">The Core Philosophy of the Program</h1>
  <div class="abs back__logo brand"><div class="brand__ring"><span class="brand__name">brightpath</span></div></div>

  <div class="abs left-col">
    <h2 class="heading">Program and upcoming dates</h2>
    <div class="dates">2 ½ Days residential<br>26th to 28th May 2019</div>
    <p class="label-it">Venue</p>
    <p class="info">The Linden Ridge Lodge,<br>Larkfield NSW</p>
    <p class="label-it" style="margin-top:4px">Future Programs</p>
    <p class="info">August, October, March</p>
    <h2 class="heading sub">Support &amp; Program Inclusions</h2>
    <p class="small">LPA Assessment, leadership skills sessions, indevidual coaching sessions, guest speakers, body wellness therapists as well as accomodation and all meals are included</p>
  </div>

  <div class="abs right-col">
    <h2 class="heading">Support &amp; Program Inclusions</h2>
    <div class="price"><span class="full">$3,495</span><span class="note">(Early Bird Book by 26th April)</span><span class="early">$3,095</span></div>
    <p class="quote">Quote QBR Code 9455<br>for a further $100 Discount</p>
  </div>

  <svg class="abs seal" viewBox="0 0 52 52" aria-hidden="true">
    <circle cx="26" cy="26" r="25" fill="#c99a2e"/>
    <circle cx="26" cy="26" r="18" fill="#222"/>
    <text x="26" y="30" text-anchor="middle" font-family="Lato,sans-serif" font-weight="700" font-size="11" fill="#e8c15a">$100</text>
  </svg>

  <div class="abs facilitator" style="left:249px">
    <div class="facilitator__photo" role="img" aria-label="Portrait photo of facilitator Dana Whitford"></div>
    <p class="facilitator__name">Dana Whitford</p>
    <p class="facilitator__role">An intuitive advisor to<br>empowered women</p>
  </div>
  <div class="abs facilitator" style="left:389px">
    <div class="facilitator__photo" role="img" aria-label="Portrait photo of facilitator Owen Castell"></div>
    <p class="facilitator__name">Owen Castell</p>
    <p class="facilitator__role">Trusted Advisor to<br>wise women</p>
  </div>

  <div class="abs back__cta">
    <p class="label">CONTACTS US NOW</p>
    <p class="num"><svg viewBox="0 0 16 16"><circle cx="8" cy="8" r="8" fill="#fff"/><path d="M5.2 4.2l1.5-.3 1 2.1-1 .8c.5 1.1 1.3 1.9 2.4 2.4l.8-1 2.1 1-.3 1.5c-3.4.3-6.8-3.1-6.5-6.5z" fill="#34a7d8"/></svg>0419372605</p>
  </div>
  <div class="abs back__contact">
    <p class="contact-row"><svg viewBox="0 0 16 16"><circle cx="8" cy="8" r="7.5" fill="#222"/><rect x="4" y="5" width="8" height="6" fill="#fff"/><path d="M4 5l4 3.2L12 5" stroke="#222" stroke-width="1" fill="none"/></svg>Info@brightpathforwardgroup.com.au</p>
    <p class="contact-row"><svg viewBox="0 0 16 16" fill="none" stroke="#222" stroke-width="1.2"><circle cx="8" cy="8" r="7"/><ellipse cx="8" cy="8" rx="3" ry="7"/><path d="M1 8h14M2.2 4.5h11.6M2.2 11.5h11.6"/></svg>brightpathforwardgroup.com.au</p>
  </div>
  <div class="abs back__strip-a"></div>
  <div class="abs back__strip-b"></div>
</section>

</body>
</html>
```